Bright Summit Web Design

I am starting a new company that will provide LIFE COACHING services - I have tried to design a website, but it's too complicated. Right now, it's just me - I'm the only person that will provide services through the website - I have used makerhive to purchase a logo (see below). I want to be able to update the website myself, but need a template - basic design. Because I am not technologically savvy enough to explain in words - I basically want to have a website that will provide basic information about my services (coaching), a page about me and my background, hopefully scheduling possibilities, and testimonials — also a page for writing/blogs. I bought a website through NetBarn - so when I have a template, I guess I”d use that - but maybe I’ll need to work with a designer to actually get it up on the internet. I have a head shot that I’ll upload, too.
Clients from the independent (private school) world - teachers, administrators
4 page

```html
<!DOCTYPE html>
<html lang="en">
<head>
<meta charset="utf-8">
<title>Bright Summit Coaching</title>
<link href="https://fonts.googleapis.com/css2?family=Montserrat:ital,wght@0,400;0,500;0,600;0,700;1,400;1,800&family=Pinyon+Script&family=Kaushan+Script&display=swap" rel="stylesheet">
<style>
:root{
  --teal:#00a19a;
  --teal-light:#5fd6c9;
  --ink:#111111;
  --white:#ffffff;
  --grey-text:#9a9a9a;
  --hero-a:#b9aa98;
  --hero-b:#7d7268;
  --dusk-a:#2d4a55;
  --dusk-b:#d98a3a;
  --dusk-c:#2c3a1e;
  --sky-top:#f2f5fa;
  --sky-mid:#9fb6d6;
  --lake:#6f8fbf;
  --sea-a:#c4632d;
  --sea-b:#1c2a3a;
}
*{margin:0;padding:0;box-sizing:border-box}
html,body{width:1200px;height:4286px;overflow:hidden;background:var(--white)}
body{position:relative;font-family:"Montserrat",sans-serif;color:var(--ink)}
.abs{position:absolute}

/* nav */
.nav-link{position:absolute;top:44px;font-size:17px;font-weight:500;color:var(--ink);text-decoration:none}
.brand-mark{position:absolute;left:553px;top:12px;width:94px;height:76px;border:2px solid var(--teal);border-radius:50%;display:flex;align-items:center;justify-content:center;font-size:11px;font-weight:500;color:var(--ink);text-align:center;line-height:1.1}

/* hero */
.hero-photo{position:absolute;left:0;top:100px;width:1200px;height:674px;background:linear-gradient(160deg,var(--hero-a),var(--hero-b) 60%,#5e5650)}
.hero-line{position:absolute;left:0;width:1200px;text-align:center;font-weight:700;font-size:53px;color:var(--ink);letter-spacing:-0.5px}
.hero-box{position:absolute;left:283px;top:508px;width:632px;height:99px;background:var(--white);display:flex;align-items:center;justify-content:center;font-size:104px;font-weight:600;letter-spacing:-3px;color:#6d6863;line-height:1}

.dot{position:absolute;left:593px;width:14px;height:14px;border-radius:50%;background:var(--teal)}

/* about */
.portrait-ring{position:absolute;left:100px;top:965px;width:370px;height:370px;border-radius:50%;border:10px dotted var(--teal)}
.portrait{position:absolute;left:128px;top:990px;width:335px;height:335px;border-radius:50%;background:radial-gradient(circle at 50% 45%,#d9c7a8,#8d8a80 70%,#5f5f5a)}
.badge{position:absolute;top:1342px;width:60px;height:60px;border-radius:8px;background:#1f4a7a}
.badge.round{border-radius:50%;background:var(--white);border:5px solid var(--teal)}
.kicker{font-style:italic;font-size:31px;color:var(--teal);font-weight:400}
.title{font-size:39px;font-weight:500;color:var(--ink);line-height:1.15}
.body-copy{font-size:18.5px;line-height:25px;color:var(--ink)}
.btn{display:inline-block;background:var(--teal-light);color:var(--ink);font-size:19px;font-weight:600;letter-spacing:2.5px;padding:6px 24px;text-transform:uppercase}

/* programs */
.programs-bg{position:absolute;left:0;top:1500px;width:1200px;height:600px;background:linear-gradient(180deg,var(--dusk-a) 0%,#6b7060 40%,var(--dusk-b) 62%,var(--dusk-c) 82%)}
.script{font-family:"Pinyon Script",cursive}
.program-card{position:absolute;left:186px;top:1746px;width:829px;height:281px;background:var(--white);border-radius:18px;overflow:hidden}
.program-photo{position:absolute;left:0;top:0;width:358px;height:244px;background:linear-gradient(135deg,#9c7a5a,#d9b04a 50%,#6d8a5e)}
.program-bar{position:absolute;left:0;bottom:0;width:100%;height:37px;background:var(--teal);color:var(--white);text-align:center;font-size:28px;letter-spacing:6px;line-height:37px}

/* retreat */
.retreat-photo{position:absolute;left:674px;top:2388px;width:403px;height:333px;border-radius:48% 52% 45% 55%;background:radial-gradient(circle at 50% 50%,#cfe0ec,#a7c2d4 55%,#eef3f6 80%)}

/* testimonials */
.testimonial-bg{position:absolute;left:0;top:2812px;width:1200px;height:549px;background:linear-gradient(180deg,var(--white) 0%,var(--sky-top) 10%,#c9d6ea 28%,var(--sky-mid) 42%,#5d6f86 52%,var(--lake) 60%,#a9bfe0 78%,var(--sky-top) 94%,var(--white) 100%)}
.testimonial-title{position:absolute;left:0;top:2940px;width:1200px;text-align:center;font-size:60px;font-weight:800;font-style:italic;color:var(--ink);letter-spacing:2px}
.quote-band{position:absolute;left:0;top:3058px;width:1200px;height:46px;background:rgba(60,60,70,.45)}
.quote{position:absolute;left:125px;top:3062px;font-family:"Kaushan Script",cursive;font-size:26px;color:var(--ink)}
.quote-author{position:absolute;left:968px;top:3100px;font-family:"Kaushan Script",cursive;font-size:28px;color:var(--teal)}

/* membership */
.member-bg{position:absolute;left:0;top:3686px;width:1200px;height:292px;background:linear-gradient(180deg,#4a3438,var(--sea-b))}
.member-top{position:absolute;left:100px;top:3470px;width:1000px;height:240px;border-radius:220px 220px 0 0;background:linear-gradient(180deg,var(--sea-a),#6a3a3a 75%,#4a3438)}
.field{position:absolute;width:446px;height:57px;background:var(--white);font-size:29px;font-weight:700;color:var(--grey-text);padding-left:20px;line-height:57px}
.subscribe{position:absolute;left:451px;top:3891px;width:311px;height:56px;background:var(--teal);color:var(--white);font-weight:700;font-size:28px;text-align:center;line-height:56px}

/* footer */
.footer-brand{position:absolute;left:502px;top:3980px;width:196px;height:196px;border:3px solid var(--teal);border-radius:50%;display:flex;align-items:center;justify-content:center;font-size:22px;font-weight:500;color:var(--ink)}
.footer-link{position:absolute;top:4176px;font-size:18px;color:var(--ink)}
.social{position:absolute;top:4230px;width:36px;height:36px;border-radius:50%;background:var(--teal)}
</style>
</head>
<body>

<!-- navigation -->
<a class="nav-link" style="left:341px">Home</a>
<a class="nav-link" style="left:442px">Blogs</a>
<div class="brand-mark">Bright Summit</div>
<a class="nav-link" style="left:700px">Services</a>
<a class="nav-link" style="left:823px">Contact Us</a>

<!-- hero -->
<div class="hero-photo" role="img" aria-label="Counsellor seated in a cosy office holding a notepad"></div>
<div class="hero-line" style="top:376px">ARE YOU HAVING A</div>
<div class="hero-line" style="top:446px">SERIOUS CRISIS?</div>
<div class="hero-box">I CAN HELP.</div>

<div class="dot" style="top:790px"></div>
<div class="dot" style="top:825px"></div>
<div class="dot" style="top:865px"></div>
<div class="dot" style="top:905px"></div>

<!-- about -->
<div class="portrait-ring"></div>
<div class="portrait" role="img" aria-label="Head shot of the counsellor smiling"></div>
<div class="badge" style="left:190px" role="img" aria-label="Certification badge"></div>
<div class="badge round" style="left:260px" role="img" aria-label="Membership badge"></div>
<div class="badge" style="left:332px" role="img" aria-label="Practitioner badge"></div>

<section class="abs" style="left:544px;top:962px;width:525px">
  <div class="kicker">Lorum Ipsum</div>
  <div class="title">About Counsellar</div>
  <p class="body-copy" style="margin-top:8px">Lorem Ipsum is simply dummy text of the printing and typesetting industry. Lorem Ipsum has been the industry's standard dummy text ever since the 1500s, when an unknown printer took a galley of type and scrambled it to make a type specimen book. It has survived not only five centuries, but also the leap into electronic typesetting, remaining essentially unchanged. It was popularised in the 1960s with the release of Letraset sheets containing.</p>
  <div class="btn" style="margin-top:14px">Learn More</div>
</section>

<!-- programs -->
<div class="programs-bg" role="img" aria-label="Sunset over a grassy field"></div>
<div class="abs script" style="left:0;top:1615px;width:1200px;text-align:center;font-size:46px;color:var(--white)">Lorum Ipsum</div>
<div class="abs" style="left:0;top:1672px;width:1200px;text-align:center;font-size:50px;font-weight:700;color:var(--white)">Our Programs</div>
<div class="program-card">
  <div class="program-photo" role="img" aria-label="Three friends laughing while looking at their phones"></div>
  <div class="abs" style="left:385px;top:16px;font-size:32px;font-weight:500">Lorum Ipsum</div>
  <p class="abs" style="left:385px;top:62px;width:420px;font-size:15.5px;line-height:21.3px">Lorem Ipsum is simply dummy text of the printing and typesetting industry. Lorem Ipsum has been the industry's standard dummy text ever since the 1500s, when an unknown printer took a galley of type and scrambled it to make a type specimen book. It has survived not only five centuries, but also the leap into electronic typesetting, remaining essentially unchanged.</p>
  <div class="program-bar">TRAINER NAME</div>
</div>

<div class="dot" style="top:2176px"></div>
<div class="dot" style="top:2213px"></div>
<div class="dot" style="top:2253px"></div>
<div class="dot" style="top:2293px"></div>

<!-- retreat -->
<section class="abs" style="left:60px;top:2398px;width:470px">
  <div class="kicker">Lorum Ipsum</div>
  <div class="title">Our Retreat</div>
  <p class="body-copy" style="margin-top:6px">Lorem Ipsum is simply dummy text of the printing and typesetting industry. Lorem Ipsum has been the industry's standard dummy text ever since the 1500s, when an unknown printer took a galley of type and scrambled it to make a type specimen book. It has survived not only five centuries, but also the leap into electronic typesetting.</p>
  <div class="btn" style="margin-top:14px">Learn More</div>
</section>
<div class="retreat-photo" role="img" aria-label="Woman stretching and relaxing with eyes closed"></div>

<!-- testimonials -->
<div class="testimonial-bg" role="img" aria-label="Snowy mountain over a lake town with autumn trees and its reflection"></div>
<div class="testimonial-title">TESTMONIALS</div>
<div class="quote-band"></div>
<div class="quote">Lorem Ipsum is simply dummy text of the printing and typesetting industry.</div>
<div class="quote-author">Dana Hollis</div>

<!-- membership -->
<div class="member-top" role="img" aria-label="Sunset sky over a rocky shore"></div>
<div class="member-bg" role="img" aria-label="Waves breaking on dark rocks"></div>
<div class="abs script" style="left:0;top:3540px;width:1200px;text-align:center;font-size:62px;color:var(--white)">Get Upto 20% Discount</div>
<div class="abs" style="left:0;top:3618px;width:1200px;text-align:center;font-size:58px;font-weight:700;color:var(--white)">MEMBERSHIP</div>
<div class="field" style="left:121px;top:3712px">NAME</div>
<div class="field" style="left:647px;top:3712px">EMAIL</div>
<div class="field" style="left:121px;top:3797px">PHONE NUMBER</div>
<div class="field" style="left:647px;top:3797px">ZIP CODE</div>
<div class="subscribe">SUBSCRIBE</div>

<!-- footer -->
<div class="footer-brand">Bright Summit</div>
<span class="footer-link" style="left:306px">Home</span>
<span class="footer-link" style="left:454px">Blogs</span>
<span class="footer-link" style="left:626px">Services</span>
<span class="footer-link" style="left:788px">Contact Us</span>
<span class="social" style="left:298px" aria-label="Social link"></span>
<span class="social" style="left:431px" aria-label="Social link"></span>
<span class="social" style="left:563px" aria-label="Social link"></span>
<span class="social" style="left:698px" aria-label="Social link"></span>
<span class="social" style="left:817px" aria-label="Social link"></span>

</body>
</html>
```